Pet and Potrait photography business needs web site design

I need a web design that is for a portrait and pet photography business based in Tasmania, Australia. It is a small, simple concept, photography business that focuses on portraits and pet photography only. I need something that is clean, maybe a white background, fun, and appealing to families. The design must make my images stand out and be the focus. The final design needs to show that it is aimed a families, pet owners, and is all about the clients - albeit the two or four legged kinds.

Business name is: maple lantern photography

I need it to be able to have the following:

- Include space for logo design which is also through SketchPlaza
- Home Page which has a gallery of my images (which you can click an arrow - either forward or back - that showcases my images
- About Page
- Portfolio Page (preferably two a) for portraits, and b) for pet photography
- Pricing page
- secure log in client page
- Contact page
Updates

Reason: Waiting for logo design to be completed to fit in with overall website design.

Target Market(s)

Families
Pet owners
Single couples who have fur babies

Industry/Entity Type

Business

Font styles to use
Serif
Decorative
Script

Colors

Designer to choose colors to be used in the design.

Requirements
Must have
• the website must provide the ability for me to upload and change images regularly.
Nice to have
• Logo design is a secondary project that will need to be worked on as well. I will pay an additional amount for those that are prepared to include this in the project.
Should not have
• No graffiti style writing.
It has to be elegant, and stylish and be aimed at females.
Women are going to be the driver for having portraits done of either their babies, children, or fur babies - i.e. pets.

```html
<!DOCTYPE html>
<html lang="en">
<head>
<meta charset="utf-8">
<title>Maple Lantern Photography</title>
<link href="https://fonts.googleapis.com/css2?family=Questrial&family=Yesteryear&family=Open+Sans:ital,wght@0,400;0,600;1,700&family=Ubuntu+Condensed&display=swap" rel="stylesheet">
<style>
:root{
  --ink:#000;
  --white:#fff;
  --accent:#ffcc00;
  --nav-muted:#9a9a9a;
  --text:#6e6e6e;
  --heading:#1a1a1a;
  --rule:#dcdcdc;
  --arrow-light:#c9c9c9;
  --arrow-dark:#3a3a3a;
}
*{margin:0;padding:0;box-sizing:border-box}
html,body{width:928px;height:1200px;overflow:hidden;background:var(--white)}
body{position:relative;font-family:"Questrial",sans-serif;color:var(--text)}
a{color:inherit;text-decoration:none}

.site-header{position:absolute;left:0;top:0;width:928px;height:111px;background:var(--ink);border-bottom:1px solid #b8a640}
.brand{position:absolute;left:108px;top:34px;color:var(--white);font-family:"Questrial",sans-serif;font-weight:400}
.brand-name{display:block;font-size:27px;letter-spacing:1px;line-height:30px}
.brand-tag{display:block;font-size:10px;letter-spacing:8.4px;margin-top:6px}

.account-links{position:absolute;right:108px;top:16px;display:flex;font-size:10px;color:var(--nav-muted)}
.account-links li{list-style:none}
.account-links li+li::before{content:"|";margin:0 14px}

.social{position:absolute;right:108px;top:42px;display:flex;gap:6px}
.social span{width:15px;height:15px;border-radius:50%;background:#4a4a4a}

.main-nav{position:absolute;right:108px;top:73px;display:flex;gap:22px;font-size:12px;color:var(--white)}
.main-nav li{list-style:none}
.main-nav .current{color:var(--accent)}

.hero{position:absolute;left:0;top:111px;width:928px;height:301px;background:linear-gradient(100deg,#6b6a4e 0%,#9b8c6c 25%,#d9b8a0 42%,#c9a88c 55%,#7b7c58 75%,#5e6e45 100%)}
.hero-arrow{position:absolute;top:232px;width:54px;height:54px;border-radius:50%;background:rgba(90,90,90,.45)}
.hero-arrow svg{position:absolute;left:19px;top:16px}
.hero-shadow{position:absolute;left:150px;top:412px;width:628px;height:26px}

.section-title{position:absolute;left:0;width:928px;text-align:center;font-family:"Yesteryear",cursive;font-size:24px;color:var(--heading)}

.gallery{position:absolute;left:109px;top:493px;width:710px;height:230px}
.tile{position:absolute;top:0;width:165px;height:199px}
.tile .photo{position:absolute;inset:0}
.overlay{position:absolute;inset:0;background:rgba(40,40,40,.72)}
.overlay svg{position:absolute;left:69px;top:57px}
.view-btn{position:absolute;left:36px;top:94px;width:94px;height:28px;border-radius:3px;background:var(--accent);color:var(--white);font-family:"Open Sans",sans-serif;font-size:11px;line-height:28px;text-align:center}
.price{position:absolute;left:52px;top:162px;width:61px;height:61px;border-radius:50%;background:var(--accent);color:var(--white);font-family:"Open Sans",sans-serif;font-style:italic;font-weight:700;font-size:14px;line-height:61px;text-align:center}
.tile.active .price{color:rgba(90,90,90,.8)}
.tile.active .price{background:rgba(255,204,0,.9)}

.testimonial-arrow{position:absolute;top:810px;width:52px;height:52px;border-radius:50%}
.testimonial-arrow svg{position:absolute;left:19px;top:17px}
.quote{position:absolute;left:272px;top:820px;width:500px;text-align:center;font-family:"Open Sans",sans-serif;font-size:10.5px;line-height:14px;color:var(--text)}
.quote-mark{font-size:14px;font-weight:600;color:#444}
.author{position:absolute;left:0;top:862px;width:928px;text-align:center;font-family:"Open Sans",sans-serif;font-size:10.5px;color:var(--text)}

.rule{position:absolute;left:108px;width:712px;height:1px;background:var(--rule)}

.footer-col{position:absolute;top:946px}
.footer-col h3{font-family:"Ubuntu Condensed",sans-serif;font-weight:400;font-size:14px;color:var(--heading);letter-spacing:.3px;margin-bottom:16px}
.footer-col li{list-style:none;font-family:"Ubuntu Condensed",sans-serif;font-size:9.5px;color:#8a7d6a;height:34px;line-height:20px;border-bottom:1px solid #e3e3e3;margin-bottom:0}
.footer-col li+li{padding-top:8px}
.footer-col li:last-child{border-bottom:none}

.copyright{position:absolute;left:108px;top:1179px;font-family:"Open Sans",sans-serif;font-size:10px;color:#555;letter-spacing:.2px}
</style>
</head>
<body>

<header class="site-header">
  <a class="brand" href="#">
    <span class="brand-name">MAPLE LANTERN</span>
    <span class="brand-tag">PHOTOGRAPHY</span>
  </a>
  <ul class="account-links">
    <li>My Account</li><li>Shopping cart</li><li>Checkout</li><li>Create an account</li>
  </ul>
  <div class="social" aria-label="Social links">
    <span></span><span></span><span></span><span></span><span></span><span></span>
  </div>
  <ul class="main-nav">
    <li class="current">HOME</li><li>ABOUT US</li><li>PORTFOLIO</li><li>PRICING</li><li>LOG IN</li><li>CONTACT</li>
  </ul>
</header>

<section class="hero" role="img" aria-label="Slideshow photo of a curly-haired little girl outdoors">
</section>
<a class="hero-arrow" style="left:51px" href="#" aria-label="Previous slide">
  <svg width="14" height="22" viewBox="0 0 14 22"><path d="M12 2 3 11l9 9" fill="none" stroke="rgba(255,255,255,.35)" stroke-width="2"/></svg>
</a>
<a class="hero-arrow" style="left:820px" href="#" aria-label="Next slide">
  <svg width="14" height="22" viewBox="0 0 14 22"><path d="M2 2l9 9-9 9" fill="none" stroke="rgba(255,255,255,.35)" stroke-width="2"/></svg>
</a>
<svg class="hero-shadow" viewBox="0 0 628 26" preserveAspectRatio="none" aria-hidden="true">
  <defs><radialGradient id="shade" cx="50%" cy="0%" r="60%"><stop offset="0" stop-color="#000" stop-opacity=".18"/><stop offset="1" stop-color="#000" stop-opacity="0"/></radialGradient></defs>
  <path d="M0 0 Q314 40 628 0Z" fill="url(#shade)"/>
</svg>

<h2 class="section-title" style="top:444px">Image Gallery</h2>

<div class="gallery">
  <div class="tile active" style="left:0">
    <div class="photo" role="img" aria-label="Portrait of a young child" style="background:linear-gradient(160deg,#c9a48c,#7c5a52 60%,#b04a6a)"></div>
    <div class="overlay">
      <svg width="30" height="30" viewBox="0 0 30 30"><circle cx="12" cy="12" r="9" fill="none" stroke="#fff" stroke-width="3"/><path d="M19 19l8 8" stroke="#fff" stroke-width="4" stroke-linecap="round"/></svg>
      <a class="view-btn" href="#">View Deatil</a>
    </div>
    <span class="price">$50.99</span>
  </div>
  <div class="tile" style="left:183px">
    <div class="photo" role="img" aria-label="Puppy and kitten together" style="background:linear-gradient(150deg,#8fa06a,#d8b47a 45%,#c99a58 70%,#6f8c4a)"></div>
    <span class="price">$50.99</span>
  </div>
  <div class="tile" style="left:366px">
    <div class="photo" role="img" aria-label="Two little sisters hugging" style="background:linear-gradient(160deg,#c9b08a,#d9a890 45%,#c9567a 75%,#9a8a6a)"></div>
    <span class="price">$50.99</span>
  </div>
  <div class="tile" style="left:545px">
    <div class="photo" role="img" aria-label="Pair of green parrots" style="background:linear-gradient(150deg,#2e4a2a,#5e9a3a 45%,#4a7a30 70%,#27351f)"></div>
    <span class="price">$50.99</span>
  </div>
</div>

<h2 class="section-title" style="top:747px">Testimonials</h2>

<a class="testimonial-arrow" style="left:56px;background:var(--arrow-light)" href="#" aria-label="Previous testimonial">
  <svg width="12" height="18" viewBox="0 0 12 18"><path d="M10 2 3 9l7 7" fill="none" stroke="#fff" stroke-width="2"/></svg>
</a>
<p class="quote"><span class="quote-mark">“</span>Proin gravida nibh vel velit auctor aliquet. Aenean sollicitudin, lorem quis bibendum auctor, nisi elit consequat ipsum, nec sagittis sem nibh id elit. Duis sed odio sit amet nibh vulputate a sit amet mauris.......<span class="quote-mark">”</span></p>
<p class="author">Ned CorwinCEO, Harbourline Pty Ltd</p>
<a class="testimonial-arrow" style="left:818px;background:var(--arrow-dark)" href="#" aria-label="Next testimonial">
  <svg width="12" height="18" viewBox="0 0 12 18"><path d="M2 2l7 7-7 7" fill="none" stroke="#fff" stroke-width="2"/></svg>
</a>

<div class="rule" style="top:915px"></div>

<footer>
  <div class="footer-col" style="left:108px;width:118px">
    <h3>INFORMATION</h3>
    <ul><li>ABOUT US</li><li>DELIVERY</li><li>PRIVACY POLICY</li><li>TERMS &amp; CONDITIONS</li></ul>
  </div>
  <div class="footer-col" style="left:292px;width:127px">
    <h3>CUSTOMER SERVICE</h3>
    <ul><li>CONTACT US</li><li>RETURNS</li><li>SITE MAP</li></ul>
  </div>
  <div class="footer-col" style="left:502px;width:127px">
    <h3>EXTRAS</h3>
    <ul><li>BRANDS</li><li>GIFT VOUCHERS</li><li>AFFILIATES</li><li>SPECIALS</li></ul>
  </div>
  <div class="footer-col" style="left:690px;width:129px">
    <h3>MY ACCOUNT</h3>
    <ul><li>MY ACCOUNT</li><li>ORDER HISTORY</li><li>WISH LIST</li><li>NEWSLETTER</li></ul>
  </div>
  <div class="rule" style="top:1166px"></div>
  <p class="copyright">Copyright © 2013 Maple Lantern Photography. All rights reserved</p>
</footer>

</body>
</html>
```